Fitness Equipment & Service

I want to make the card eye catching and fun. We are called Corvane Motion Limited and we are based in Wales. We sell, install and service all types of fitness equipment from Skipping ropes, right through the Dumbbells, Kettle bells and Barbells through to state of the art Treadmills, Running Machines and Strength Equipment. We also design and install changing room furniture and lockers.

TYPOGRAPHY
We would like to use Futrura. Futura has an appearance of efficiency and forwardness. The typeface is derived
from simple geometric forms (near-perfect circles, triangles and squares) and is based on strokes of
near-even weight, which are low in contrast. This is most visible in the almost perfectly round stroke of
the o, which is nonetheless slightly ovoid.
The lowercase has tall ascenders, which rise above the cap line. The uppercase
characters present proportions similar to those of classical Roman capitals.

TYPOGRAPHIC CONSIDERATIONS
No Strike though
No Horizontal Scaling
No Drop Shadows
No Effects
Never use less than 120% Leading

OUR CORPORATE COLOURS
BRAND GUIDELINES
We were thinking that our primary colour palette consists of the Acid Green (Pantone 382) and Process Black.

We work closely with tolbrook Ltd and would like to include their name on the card somewhere. I have attached images of the other brands that we work with as an idea or the small icons I have included that illustrate what we do?. I have very kindly been given permission to use any of the images off the files that I have included below, so I hope these help. I will include these below. I would be open to suggestions if it made the card more striking Can you do it?
Updates

Hi All, Just wanted to add a few thoughts but you are the guys with the creative visions (thats why are here) We are based in Wales, UK and we would be open to lots of different ideas on a theme but must be eye catching, Bold and FUN. If you can or think that the Welsh or any dragon could be put in there then go for it (its not a must have) We have also added some ideas for colour but again its over to you!! GO FOR IT ! Thanks and look forward to your visions! Owen

Hi All, Just thought I would sen through the contact details that need to be on the card. (if you want to play around with icons instead of the wording twitter, Facebook, go for it): Corvane Motion Limited Owen Pritchard Managing Director Mob: +44 (0)7382 519 046 e-mail: sales@corvanemotion.co.uk Web: Corvanemotion.co.uk twitter: @motionPostbag Facebook: Corvane Motion Limited

Industry/Entity Type

Fitness

```html
<!DOCTYPE html>
<html lang="en">
<head>
<meta charset="utf-8">
<title>Corvane Motion Limited – Business Card</title>
<link rel="stylesheet" href="https://fonts.googleapis.com/css2?family=Arimo:wght@400;700&display=swap">
<style>
  :root {
    --page-bg: #e4e4e2;
    --card-top: #ffffff;
    --card-bottom: #ebebeb;
    --ink: #111111;
    --acid: #c4d600;
    --acid-dark: #8a9a00;
    --text-grey: #3a3a3a;
    --rule: #9aa0a0;
  }
  * { box-sizing: border-box; margin: 0; padding: 0; }
  html, body {
    width: 1200px; height: 950px; overflow: hidden;
    background: var(--page-bg);
    font-family: "Arimo", Arial, sans-serif;
  }
  .card {
    position: absolute; left: 232px;
    width: 736px; height: 420px;
    background: linear-gradient(160deg, var(--card-top) 0%, var(--card-bottom) 100%);
    box-shadow: 0 10px 30px rgba(0,0,0,.16);
  }
  .card-back { top: 36px; }
  .card-front { top: 494px; }

  /* back */
  .back-emblem {
    position: absolute; left: 288px; top: 60px;
    width: 160px; height: 160px;
  }
  .back-brand {
    position: absolute; left: 0; right: 0; top: 246px;
    display: flex; justify-content: center; align-items: center; gap: 12px;
    color: var(--ink); font-weight: 700; font-size: 24px; line-height: 1.2;
  }
  .back-web {
    position: absolute; right: 40px; top: 340px;
    display: flex; align-items: center; gap: 12px;
    color: var(--text-grey); font-size: 17px; line-height: 1.3; letter-spacing: .5px;
  }
  .back-web::after {
    content: ""; width: 60px; height: 2px; background: var(--rule);
  }

  /* front */
  .brand {
    position: absolute; left: 40px; top: 34px;
    color: var(--ink); font-weight: 700;
    font-size: 25px; line-height: 1.2;
    display: flex; align-items: center; gap: 12px;
  }
  .brand-mark {
    width: 20px; height: 20px; border-radius: 50%;
    background: var(--acid);
  }
  .person { position: absolute; left: 40px; top: 106px; }
  .person-name { color: var(--ink); font-weight: 700; font-size: 25px; line-height: 1.2; }
  .person-role { color: var(--acid-dark); font-size: 19px; line-height: 1.25; }
  .address {
    position: absolute; left: 40px; top: 178px;
    color: var(--text-grey); font-size: 17px; line-height: 1.3;
  }
  .contacts {
    position: absolute; left: 40px; top: 234px;
    list-style: none; color: var(--text-grey);
    font-size: 17px; line-height: 1.3;
  }
  .contacts li { display: flex; align-items: center; gap: 10px; height: 23px; }
  .contacts svg { width: 15px; height: 15px; flex: none; }
  .emblem-area {
    position: absolute; left: 430px; top: 86px;
    width: 260px; height: 260px;
  }
</style>
</head>
<body>
  <div class="card card-back">
    <svg class="back-emblem" viewBox="0 0 160 160" role="img" aria-label="Company emblem area">
      <defs>
        <radialGradient id="backFill" cx="45%" cy="40%" r="60%">
          <stop offset="0%" stop-color="var(--acid)"/>
          <stop offset="100%" stop-color="var(--ink)"/>
        </radialGradient>
      </defs>
      <circle cx="80" cy="80" r="76" fill="url(#backFill)"/>
    </svg>
    <div class="back-brand"><span>Corvane Motion Limited</span></div>
    <div class="back-web">corvanemotion.co.uk</div>
  </div>

  <div class="card card-front">
    <div class="brand"><span class="brand-mark"></span><span>Corvane Motion Limited</span></div>

    <div class="person">
      <div class="person-name">Owen Pritchard</div>
      <div class="person-role">Managing Director</div>
    </div>

    <div class="address">
      <div>27 Harbour Row</div>
      <div>Cardiff, CF10 4PL</div>
    </div>

    <ul class="contacts">
      <li>
        <svg viewBox="0 0 20 20" aria-hidden="true"><rect x="5" y="1" width="10" height="18" rx="2" fill="var(--ink)"/><rect x="7" y="3.5" width="6" height="11" fill="#fff"/><circle cx="10" cy="16.7" r="1" fill="#fff"/></svg>
        <span>+44 (0)7382 519 046</span>
      </li>
      <li>
        <svg viewBox="0 0 20 20" aria-hidden="true"><rect x="1" y="4" width="18" height="12" rx="1.5" fill="var(--ink)"/><path d="M2 5 L10 11 L18 5" stroke="#fff" stroke-width="1.5" fill="none"/></svg>
        <span>sales@corvanemotion.co.uk</span>
      </li>
      <li>
        <svg viewBox="0 0 20 20" aria-hidden="true"><circle cx="10" cy="10" r="8.5" fill="var(--ink)"/><ellipse cx="10" cy="10" rx="3.5" ry="8.5" stroke="#fff" stroke-width="1.2" fill="none"/><path d="M1.5 10 H18.5" stroke="#fff" stroke-width="1.2"/></svg>
        <span>Corvanemotion.co.uk</span>
      </li>
      <li>
        <svg viewBox="0 0 20 20" aria-hidden="true"><rect x="2" y="2" width="16" height="16" rx="2" fill="var(--ink)"/></svg>
        <span>@motionPostbag</span>
      </li>
      <li>
        <svg viewBox="0 0 20 20" aria-hidden="true"><rect x="2" y="2" width="16" height="16" rx="2" fill="var(--ink)"/></svg>
        <span>Corvane Motion Limited</span>
      </li>
    </ul>

    <svg class="emblem-area" viewBox="0 0 260 260" role="img" aria-label="Large company emblem area">
      <defs>
        <radialGradient id="frontFill" cx="45%" cy="40%" r="60%">
          <stop offset="0%" stop-color="var(--acid)"/>
          <stop offset="100%" stop-color="var(--ink)"/>
        </radialGradient>
      </defs>
      <circle cx="130" cy="130" r="124" fill="url(#frontFill)"/>
    </svg>
  </div>
</body>
</html>
```